Residential Construction Business - Site Signage

I need a design made for a site fence banner. We have a logo and branding so the design would need to be aligned with this. It would need to be made to specific size ratio so that it can be sent to the maker for production.
ratio : 4600 wide x 1700 high
The design should feature our website and also the slogan
"don't move, re-imagine"

Target Market(s)

potential clients

Industry/Entity Type

construction

Font styles to use
Other font styles liked:
• to match branding

Colors
0054AA
0677BA
7BADD7
CADEEF
E8F1F8

Requirements
Must have
• www.velmbuild.com.au Majority of the sign is our brand logo
Nice to have
• Majority of the sign is our brand logo
Should not have
• colors and themes that arent brand relevant

```html
<!DOCTYPE html>
<html lang="en">
<head>
<meta charset="utf-8">
<title>Velm Build – Site Fence Banner</title>
<link rel="stylesheet" href="https://fonts.googleapis.com/css2?family=Montserrat:ital,wght@0,500;0,600;0,700;1,600&display=swap">
<style>
  :root {
    --brand-navy: #053f5e;
    --paper: #ffffff;
    --backdrop: #e6e6e6;
  }
  * { margin: 0; padding: 0; box-sizing: border-box; }
  html, body {
    width: 1200px;
    height: 675px;
    overflow: hidden;
    background: var(--backdrop);
    font-family: "Montserrat", Arial, sans-serif;
  }
  .banner {
    position: absolute;
    left: 40px;
    top: 130px;
    width: 1120px;
    height: 414px;
    background: var(--paper);
  }
  .banner__field {
    position: absolute;
    left: 0;
    top: 0;
    width: 1120px;
    height: 358px;
    background: var(--brand-navy);
  }
  .brand-block {
    position: absolute;
    left: 62px;
    top: 53px;
    width: 254px;
    height: 254px;
    background: var(--paper);
  }
  .brand-name {
    position: absolute;
    left: 346px;
    top: 162px;
    color: var(--paper);
    font-weight: 700;
    font-size: 34px;
    letter-spacing: 12px;
    line-height: 1;
    white-space: nowrap;
  }
  .slogan {
    position: absolute;
    left: 786px;
    top: 134px;
    color: var(--paper);
    font-weight: 500;
    font-size: 37px;
    line-height: 44px;
    white-space: nowrap;
  }
  .slogan em {
    font-style: italic;
    font-weight: 600;
  }
  .banner__strip {
    position: absolute;
    left: 0;
    top: 358px;
    width: 1120px;
    height: 56px;
    display: flex;
    align-items: center;
    justify-content: center;
  }
  .website {
    color: var(--brand-navy);
    font-weight: 600;
    font-size: 32px;
    letter-spacing: 5px;
    line-height: 1;
  }
</style>
</head>
<body>
  <main class="banner">
    <section class="banner__field">
      <div class="brand-block" aria-hidden="true"></div>
      <div class="brand-name">VELM BUILD</div>
      <p class="slogan">Don't Move,<br>Re-<em>Imagine</em></p>
    </section>
    <footer class="banner__strip">
      <span class="website">www.velmbuild.com.au</span>
    </footer>
  </main>
</body>
</html>
```